Media and Film Company Needs a New Website

We produce highly stylized commercials and film pieces for our clients. We also produce live events, both corporate and theatrical. Looking for a site that can show off our client videos - have a polished way to show off our team, and be able to create pages to highlight our clients and give a full overview of our project/process with them. We design simple website for some of our clients - so we are very wordpress familiar, and would like something that doesn't feel like a template.

Target Market(s)

content creators, creative directors, production teams, marketing agencies

Industry/Entity Type

Film Production

Number of Pages Required

4 page

Font styles to use
Sans Serif

Requirements
Must have
• slick looking video embed (from YT or Vimeo)
• project pages - client snapshot (what we did for them, how we did it)
• nice landing page, have our company video reel on the page
• testimonials
• contact page
• ability to have photos as a background if we want
Nice to have
• polished clean look - look to our logo colors and linear elements
• we produce very stylized videos for our clients and our website should reflect that
Should not have
• template look or feel to it- please bring your flare to the project!
• take a look at our current site - brelvostudio.com we need a better way to highlight our work and our clients

```html
<!DOCTYPE html>
<html lang="en">
<head>
<meta charset="utf-8">
<title>Brelvo Studio — Home</title>
<link rel="stylesheet" href="https://fonts.googleapis.com/css2?family=Open+Sans:wght@300;400;600;700&family=Lato:wght@300;400;700;900&family=Pacifico&display=swap">
<style>
:root{
  --blue-deep:#0a62e8;
  --blue-light:#4aa6ff;
  --accent-blue:#2e8ef0;
  --pink:#e8457a;
  --yellow:#f2c511;
  --green:#86b83a;
  --teal:#1aa38a;
  --purple:#7a3fb8;
  --orange:#f39c12;
  --ink:#333;
  --muted:#777;
  --line:#d9d9d9;
  --card-foot:#5d5d5d;
  --footer:#0e0e0e;
  --white:#fff;
}
*{box-sizing:border-box;margin:0;padding:0}
html,body{width:1200px;height:2675px;overflow:hidden}
body{position:relative;background:var(--white);font-family:"Open Sans",Arial,sans-serif;color:var(--ink)}
.abs{position:absolute}

/* hero */
.hero{position:absolute;left:0;top:0;width:1200px;height:501px;background:radial-gradient(ellipse at 50% 30%,var(--blue-light) 0%,var(--blue-deep) 70%)}
.topbar-phone{left:234px;top:4px;font-size:10px;color:var(--white);display:flex;align-items:center;gap:8px}
.topbar-search{left:955px;top:4px}
.navbar{left:237px;top:25px;width:729px;height:50px;background:var(--white);display:flex;align-items:center;padding:0 14px}
.brand{font-family:"Lato",sans-serif;font-weight:900;font-size:20px;letter-spacing:.5px;color:#111;display:flex;align-items:center;gap:8px}
.brand-dot{width:12px;height:12px;background:var(--pink)}
.nav{margin-left:auto;display:flex;gap:25px;font-family:"Lato",sans-serif;font-weight:700;font-size:11px;color:#222}
.nav .active{color:var(--pink)}
.hero-title{left:0;width:1200px;top:150px;text-align:center;font-family:"Lato",sans-serif;font-weight:900;font-size:80px;color:var(--white);letter-spacing:1px;line-height:1}
.video{left:226px;top:267px;width:434px;height:250px;background:linear-gradient(#2a2a2a,#1a1a1a);box-shadow:0 14px 22px rgba(0,0,0,.35)}
.video-reel{left:42px;top:150px;font-family:"Open Sans",sans-serif;font-weight:300;font-size:46px;color:#ddd}
.video-controls{left:12px;bottom:8px;width:410px;height:16px;display:flex;align-items:center;gap:10px}
.video-track{flex:1;height:3px;background:#555}
.video-side-title{left:664px;top:262px;font-family:"Pacifico",cursive;font-size:19px;color:var(--white)}
.video-side-list{left:674px;top:308px;font-size:9px;color:var(--white);line-height:15px;list-style:disc}
.btn-contact{left:672px;top:487px;width:86px;height:25px;background:#222;color:var(--white);font-family:"Lato",sans-serif;font-weight:700;font-size:10px;display:flex;align-items:center;justify-content:center;letter-spacing:.5px}
.btn-mail{left:768px;top:487px;width:25px;height:25px;background:#222;display:flex;align-items:center;justify-content:center}

/* section heads */
.section-title{font-family:"Open Sans",sans-serif;font-weight:300;font-size:32px;color:#222;letter-spacing:.5px}
.section-title .count{margin-right:16px}
.outline-btn{width:139px;height:30px;border:2px solid;display:flex;align-items:center;justify-content:center;font-family:"Lato",sans-serif;font-weight:700;font-size:11px;letter-spacing:.5px}

/* services */
.service{width:175px}
.service-icon{position:absolute;left:0;top:0;width:56px;height:44px;border-radius:6px}
.service-head{position:absolute;left:66px;top:8px;font-family:"Lato",sans-serif;font-weight:900;font-size:12px;line-height:15px;color:#333;white-space:nowrap}
.service-rule{position:absolute;left:66px;top:53px;width:32px;height:3px}
.service-list{position:absolute;left:66px;top:78px;list-style:none;font-size:9.5px;color:var(--accent-blue);line-height:19.5px;white-space:nowrap}

/* stats */
.stat{width:124px;height:124px;border-radius:50%;border:2px solid var(--accent-blue);border-right-color:#cfe4fb;display:flex;flex-direction:column;align-items:center;justify-content:center;color:var(--accent-blue)}
.stat-num{font-weight:300;font-size:32px;line-height:1}
.stat-label{font-size:9px;margin-top:6px;color:#3a7cc5}

/* projects */
.card{width:218px;height:210px;background:var(--card-foot)}
.card-photo{position:absolute;left:0;top:0;width:100%;height:130px}
.card-link{position:absolute;left:50%;top:42px;margin-left:-23px;width:46px;height:46px;border-radius:50%;background:rgba(255,255,255,.85);display:flex;align-items:center;justify-content:center}
.card-tag{position:absolute;left:12px;top:143px;height:17px;padding:0 10px;font-size:7.5px;font-weight:700;color:var(--white);display:flex;align-items:center;white-space:nowrap}
.card-date{position:absolute;right:12px;top:146px;font-size:7.5px;color:var(--white)}
.card-title{position:absolute;left:12px;top:168px;right:10px;font-family:"Lato",sans-serif;font-weight:900;font-size:12px;line-height:15px;color:var(--white)}
.arrow{width:38px;height:20px}

/* clients */
.client{font-family:"Lato",sans-serif;font-weight:900;font-size:15px;color:#444;display:flex;align-items:center;gap:6px;white-space:nowrap}
.client-mark{width:12px;height:12px;background:#444;border-radius:50%}

/* cta */
.cta{left:0;top:1712px;width:1200px;height:271px;background:linear-gradient(90deg,#3a3634 0%,#4a3a30 55%,#2d2622 100%)}
.cta-line1{left:246px;top:70px;font-weight:300;font-size:31px;color:var(--white)}
.cta-line2{left:246px;top:102px;font-family:"Lato",sans-serif;font-weight:900;font-size:37px;color:var(--accent-blue)}
.field{top:164px;width:164px;height:30px;background:var(--white);font-size:9px;color:#888;padding:0 10px;display:flex;align-items:center}
.btn-coop{left:813px;top:162px;width:139px;height:32px;border:2px solid var(--white);color:var(--white);font-family:"Lato",sans-serif;font-weight:700;font-size:11px;display:flex;align-items:center;justify-content:center}

/* testimonials */
.quote{width:220px;text-align:center}
.avatar{width:50px;height:50px;border-radius:50%;background:#c8c8c8;margin:0 auto}
.quote-name{margin-top:16px;font-family:"Lato",sans-serif;font-weight:700;font-size:13px;color:#333}
.quote-org{font-size:9px;color:var(--accent-blue);margin-top:1px}
.quote-rule{width:24px;height:2px;margin:9px auto 10px}
.quote-text{font-size:9.5px;line-height:17.5px;color:#888}

/* footer */
.footer{left:0;top:2462px;width:1200px;height:213px;background:var(--footer)}
.social{top:70px;width:22px;height:22px;border:2px solid;transform:rotate(45deg)}
.copyright{left:0;width:1200px;top:131px;text-align:center;font-size:8.5px;color:#aaa;letter-spacing:.3px}
</style>
</head>
<body>

<header class="hero">
  <div class="abs topbar-phone">
    <svg width="9" height="9" viewBox="0 0 10 10"><path d="M2 0l2 2-1 2c1 1 2 2 3 3l2-1 2 2-2 2C4 10 0 6 0 2z" fill="#fff"/></svg>
    0155-20-41-7730
  </div>
  <svg class="abs topbar-search" width="10" height="10" viewBox="0 0 10 10"><circle cx="4" cy="4" r="3" stroke="#fff" stroke-width="1.5" fill="none"/><path d="M6.5 6.5L9.5 9.5" stroke="#fff" stroke-width="1.5"/></svg>

  <nav class="abs navbar">
    <div class="brand"><span class="brand-dot"></span>BRELVO STUDIO</div>
    <div class="nav">
      <span class="active">HOME</span><span>PORTFOLIO</span><span>ABOUT BRELVO</span><span>TESTIMONIALS</span><span>PRESS</span><span>CONTACT US</span>
    </div>
  </nav>

  <h1 class="abs hero-title">WELCOME TO BRELVO</h1>

  <div class="abs video" role="img" aria-label="Company demo reel video player">
    <div class="abs video-reel">2015 Demo Reel</div>
    <div class="abs video-controls">
      <svg width="9" height="10" viewBox="0 0 9 10"><path d="M0 0L9 5 0 10z" fill="#fff"/></svg>
      <span style="font-size:7px;color:#ccc">00:00</span>
      <div class="video-track"></div>
      <svg width="30" height="8" viewBox="0 0 30 8"><rect x="0" y="5" width="2" height="3" fill="#f39c12"/><rect x="3" y="3" width="2" height="5" fill="#f39c12"/><rect x="6" y="1" width="2" height="7" fill="#f39c12"/><text x="11" y="7.5" font-size="7" fill="#fff" font-family="Arial,sans-serif">HD</text></svg>
    </div>
  </div>
  <div class="abs video-side-title">About Brelvo Studio video title</div>
  <ul class="abs video-side-list">
    <li>Video Description 1 here</li>
    <li>Video Description 2 here</li>
  </ul>
  <div class="abs btn-contact">CONTACT US</div>
  <div class="abs btn-mail"><svg width="12" height="9" viewBox="0 0 12 9"><rect x=".5" y=".5" width="11" height="8" fill="none" stroke="#fff"/><path d="M.5 .5L6 5l5.5-4.5" fill="none" stroke="#fff"/></svg></div>
</header>

<section>
  <h2 class="abs section-title" style="left:246px;top:622px">WHAT WE DO</h2>

  <div class="abs service" style="left:242px;top:700px">
    <div class="service-icon" role="img" aria-label="Film and media production illustration" style="background:linear-gradient(135deg,#f6a04d,#e8457a)"></div>
    <div class="service-head">FILM &amp; MEDIA<br>PRODUCTION</div>
    <div class="service-rule" style="background:var(--teal)"></div>
    <ul class="service-list"><li>DESIGN SOFTWARE SUITE</li><li>MOTION GRAPHICS</li><li>4K WORKFLOW</li><li>DIRECT TO WEB/STREAMING</li></ul>
  </div>
  <div class="abs service" style="left:419px;top:700px">
    <div class="service-icon" role="img" aria-label="Live production illustration" style="background:linear-gradient(135deg,#f4d04a,#7fb4e8)"></div>
    <div class="service-head">LIVE<br>PRODUCTION</div>
    <div class="service-rule" style="background:var(--orange)"></div>
    <ul class="service-list"><li>THEATRICAL PRODUCING</li><li>PRODUCTION MANAGEMENT</li><li>LIGHTING &amp; VIDEO DESIGN</li><li>AUDIO SYS_EM DESIGN</li></ul>
  </div>
  <div class="abs service" style="left:594px;top:700px">
    <div class="service-icon" role="img" aria-label="PR, marketing and advertising illustration" style="background:linear-gradient(135deg,#f39c12,#3a8de0)"></div>
    <div class="service-head">PD,MARKENTING<br>&amp; ADVERTISING</div>
    <div class="service-rule" style="background:#a9c93a"></div>
    <ul class="service-list"><li>BRANDING</li><li>SOCIAL MEDIA</li><li>MED A RELATIONS AND OUTREACH</li><li>STREET TEAMS</li></ul>
  </div>
  <div class="abs service" style="left:772px;top:700px">
    <div class="service-head" style="left:70px;top:16px">EVENTS</div>
    <div class="service-rule" style="left:70px;background:var(--purple)"></div>
    <ul class="service-list" style="left:70px"><li>EVENT PRODUCTION</li><li>STAFFING &amp; HIRING</li><li>MANAGE RFPS</li><li>SPONSOR RELATIONS</li></ul>
  </div>

  <div class="abs stat" style="left:273px;top:936px"><span class="stat-num">82</span><span class="stat-label">EQUIPMENTS</span></div>
  <div class="abs stat" style="left:450px;top:936px"><span class="stat-num">92</span><span class="stat-label">CREATIVE</span></div>
  <div class="abs stat" style="left:624px;top:936px"><span class="stat-num">76</span><span class="stat-label">SPEED</span></div>
  <div class="abs stat" style="left:803px;top:936px"><span class="stat-num">96</span><span class="stat-label">QUALITY</span></div>
</section>

<section>
  <h2 class="abs section-title" style="left:246px;top:1110px"><span class="count" style="color:var(--accent-blue)">214</span>PROJECTS</h2>
  <div class="abs outline-btn" style="left:813px;top:1118px;border-color:var(--accent-blue);color:var(--accent-blue)">VISIT PORTFOLIO</div>

  <article class="abs card" style="left:-84px;top:1225px">
    <div class="card-photo" style="background:#cfcfcf" role="img" aria-label="Project still"></div>
    <span class="card-tag" style="left:40px;background:var(--purple)">PRODUCTION</span>
    <span class="card-date">SEPTEMBER 2016</span>
    <div class="card-title" style="left:84px">electromagnetic brain</div>
  </article>
  <article class="abs card" style="left:248px;top:1225px">
    <div class="card-photo" style="background:linear-gradient(135deg,#8a7462,#3e3a36)" role="img" aria-label="Live production project photo"></div>
    <div class="card-link"><svg width="22" height="22" viewBox="0 0 22 22"><rect x="3" y="8" width="9" height="6" rx="3" transform="rotate(-45 7.5 11)" fill="none" stroke="#555" stroke-width="2"/><rect x="10" y="8" width="9" height="6" rx="3" transform="rotate(-45 14.5 11)" fill="none" stroke="#555" stroke-width="2"/></svg></div>
    <span class="card-tag" style="background:var(--green)">LIVE PRODUCTION</span>
    <span class="card-date">SEPTEMBER 2015</span>
    <div class="card-title">Description or title would look great here</div>
  </article>
  <article class="abs card" style="left:492px;top:1225px">
    <div class="card-photo" style="background:linear-gradient(180deg,#2a3f8f,#5b7fd1)" role="img" aria-label="Events production project photo"></div>
    <div class="card-link"><svg width="22" height="22" viewBox="0 0 22 22"><rect x="3" y="8" width="9" height="6" rx="3" transform="rotate(-45 7.5 11)" fill="none" stroke="#555" stroke-width="2"/><rect x="10" y="8" width="9" height="6" rx="3" transform="rotate(-45 14.5 11)" fill="none" stroke="#555" stroke-width="2"/></svg></div>
    <span class="card-tag" style="background:var(--teal)">EVENTS PRODUCTION</span>
    <span class="card-date">MARCH 2015</span>
    <div class="card-title">Description or title would look great here</div>
  </article>
  <article class="abs card" style="left:735px;top:1225px">
    <div class="card-photo" style="background:linear-gradient(135deg,#3a5aa8,#1c2f66)" role="img" aria-label="Film production project photo"></div>
    <div class="card-link"><svg width="22" height="22" viewBox="0 0 22 22"><rect x="3" y="8" width="9" height="6" rx="3" transform="rotate(-45 7.5 11)" fill="none" stroke="#555" stroke-width="2"/><rect x="10" y="8" width="9" height="6" rx="3" transform="rotate(-45 14.5 11)" fill="none" stroke="#555" stroke-width="2"/></svg></div>
    <span class="card-tag" style="background:var(--pink)">FILM PRODUCTION</span>
    <span class="card-date">JUNE 2015</span>
    <div class="card-title">Description or title would look great here</div>
  </article>
  <article class="abs card" style="left:1066px;top:1225px">
    <div class="card-photo" style="background:#cfcfcf" role="img" aria-label="Project still"></div>
    <span class="card-tag" style="background:var(--orange)">EVENT STAFFING</span>
    <div class="card-title">Draft of the new district Monaco</div>
  </article>

  <svg class="abs arrow" style="left:246px;top:1481px" viewBox="0 0 38 20"><path d="M37 10H2M10 2L2 10l8 8" fill="none" stroke="#333" stroke-width="1.5"/></svg>
  <svg class="abs arrow" style="left:916px;top:1481px" viewBox="0 0 38 20"><path d="M1 10h35M28 2l8 8-8 8" fill="none" stroke="#333" stroke-width="1.5"/></svg>
</section>

<section>
  <h2 class="abs section-title" style="left:260px;top:1538px"><span class="count" style="color:var(--pink)">17</span>CLIENTS</h2>
  <div class="abs outline-btn" style="left:813px;top:1542px;border-color:var(--pink);color:var(--pink)">HERE'S MORE</div>

  <div class="abs client" style="left:303px;top:1632px">Northgate Docs</div>
  <div class="abs client" style="left:438px;top:1632px">Pellar Group</div>
  <div class="abs client" style="left:548px;top:1632px">Verano Music</div>
  <div class="abs client" style="left:662px;top:1632px"><span class="client-mark"></span>Quillbox</div>
  <div class="abs client" style="left:760px;top:1632px">Fentrio</div>
  <div class="abs client" style="left:822px;top:1632px">Oakhaven</div>
</section>

<section class="abs cta" role="img" aria-label="Background photo of a desk with a calendar and film equipment">
  <div class="abs cta-line1">START WORKING WITH US</div>
  <div class="abs cta-line2">RIGHT NOW!</div>
  <div class="abs field" style="left:246px">NAME</div>
  <div class="abs field" style="left:424px">E-MAIL</div>
  <div class="abs btn-coop">START COOPERATION</div>
</section>

<section>
  <h2 class="abs section-title" style="left:246px;top:2053px"><span class="count" style="color:var(--yellow)">24</span>TESTIMONIALS</h2>
  <div class="abs outline-btn" style="left:813px;top:2058px;border-color:var(--yellow);color:var(--yellow)">READ MORE</div>

  <div class="abs quote" style="left:247px;top:2124px">
    <div class="avatar"></div>
    <div class="quote-name">Clara Venholt</div>
    <div class="quote-org">Ardent Holdings Ltd</div>
    <div class="quote-rule" style="background:var(--pink)"></div>
    <p class="quote-text">This little clear crystal mouse is so happy with her little cheese in Light Topaz crystal! The delicate whiskers, tail and ears show great attention to detaillittle cheese in Light Topaz crystal!</p>
  </div>
  <div class="abs quote" style="left:489px;top:2124px">
    <div class="avatar"></div>
    <div class="quote-name">Ravi Denmarr</div>
    <div class="quote-org">Lumen India</div>
    <div class="quote-rule" style="background:var(--teal)"></div>
    <p class="quote-text">This little clear crystal mouse is so happy with her little cheese in Light Topaz crystal! The delicate whiskers, tail and ears show great attention to detail. This little clear crystal mouse is so happy with her little cheese in Light Topaz crystal!</p>
  </div>
  <div class="abs quote" style="left:733px;top:2124px">
    <div class="avatar"></div>
    <div class="quote-name">TR Hallowell</div>
    <div class="quote-org">Veltrano</div>
    <div class="quote-rule" style="background:var(--accent-blue)"></div>
    <p class="quote-text">This little clear crystal mouse is so happy with her little cheese in Light Topaz crystal! The delicate whiskers, tail and ears show great attention to detail.</p>
  </div>

  <svg class="abs arrow" style="left:246px;top:2392px" viewBox="0 0 38 20"><path d="M37 10H2M10 2L2 10l8 8" fill="none" stroke="#333" stroke-width="1.5"/></svg>
  <svg class="abs arrow" style="left:916px;top:2392px" viewBox="0 0 38 20"><path d="M1 10h35M28 2l8 8-8 8" fill="none" stroke="#333" stroke-width="1.5"/></svg>
</section>

<footer class="abs footer">
  <span class="abs social" style="left:549px;border-color:var(--pink)"></span>
  <span class="abs social" style="left:588px;border-color:var(--accent-blue)"></span>
  <span class="abs social" style="left:627px;border-color:#3b5fb5"></span>
  <div class="abs copyright">©2017 BRELVO STUDIO</div>
  <svg class="abs" style="left:586px;top:193px" width="28" height="20" viewBox="0 0 28 20"><path d="M14 0L28 20H0z" fill="var(--yellow)"/></svg>
</footer>

</body>
</html>
```